Accounting firm needing business card / letterhead designed
Marcus T. Elbering, CPA
marcus@fernquill.com
www.fernquill.com
482 N Harlow Ave Corvale, IN 43719
555-310-0172

```html
<!DOCTYPE html>
<html lang="en">
<head>
<meta charset="utf-8">
<title>Fernquill – Business Card</title>
<link rel="stylesheet" href="https://fonts.googleapis.com/css2?family=Open+Sans:wght@400;600;700&display=swap">
<style>
  :root {
    --navy: #262262;
    --green: #8dc63f;
    --white: #ffffff;
    --backdrop: #ecedf0;
    --disc-edge: #e6e8eb;
  }
  * { box-sizing: border-box; margin: 0; padding: 0; }
  html, body {
    width: 1200px;
    height: 900px;
    overflow: hidden;
    background: var(--backdrop);
    font-family: "Open Sans", Arial, sans-serif;
  }
  .canvas {
    position: relative;
    width: 1200px;
    height: 900px;
  }
  .business-card {
    position: absolute;
    left: 112px;
    top: 150px;
    width: 975px;
    height: 600px;
    border-radius: 22px;
    overflow: hidden;
    background: var(--navy);
    box-shadow: 0 10px 30px rgba(20, 20, 60, 0.18);
  }
  .accent-band {
    position: absolute;
    top: 0;
    right: 0;
    width: 300px;
    height: 100%;
    background: var(--green);
  }
  .brand-disc {
    position: absolute;
    left: 418px;
    top: 42px;
    width: 516px;
    height: 516px;
    border-radius: 50%;
    background: radial-gradient(circle at 45% 40%, #ffffff 0%, #f6f7f8 55%, var(--disc-edge) 100%);
    display: flex;
    align-items: center;
    justify-content: center;
  }
  .brand-name {
    font-weight: 700;
    font-size: 70px;
    letter-spacing: 4px;
    color: var(--navy);
    text-transform: uppercase;
  }
  .holder-name {
    position: absolute;
    left: 54px;
    top: 76px;
    font-weight: 600;
    font-size: 32px;
    color: var(--green);
    text-transform: uppercase;
    letter-spacing: 0.5px;
    white-space: nowrap;
  }
  .address {
    position: absolute;
    left: 54px;
    top: 318px;
    font-size: 24px;
    line-height: 36px;
    color: var(--white);
  }
  .contact-list {
    position: absolute;
    left: 54px;
    top: 412px;
    list-style: none;
  }
  .contact-item {
    display: flex;
    align-items: center;
    gap: 10px;
    font-size: 24px;
    line-height: 36px;
    color: var(--white);
  }
  .contact-icon {
    width: 22px;
    height: 22px;
    fill: var(--green);
    flex: none;
  }
</style>
</head>
<body>
<main class="canvas">
  <article class="business-card">
    <div class="accent-band"></div>
    <div class="brand-disc">
      <span class="brand-name">Fernquill</span>
    </div>

    <h1 class="holder-name">Marcus T. Elbering, CPA</h1>

    <p class="address">482 N Harlow Ave Corvale,<br>IN 43719</p>

    <ul class="contact-list">
      <li class="contact-item">
        <svg class="contact-icon" viewBox="0 0 24 24" aria-hidden="true">
          <path d="M6.6 10.8c1.4 2.8 3.8 5.1 6.6 6.6l2.2-2.2c.3-.3.7-.4 1-.2 1.1.4 2.3.6 3.6.6.6 0 1 .4 1 1V20c0 .6-.4 1-1 1C10.6 21 3 13.4 3 4c0-.6.4-1 1-1h3.5c.6 0 1 .4 1 1 0 1.3.2 2.5.6 3.6.1.3 0 .7-.2 1l-2.3 2.2z"/>
        </svg>
        555-310-0172
      </li>
      <li class="contact-item">
        <svg class="contact-icon" viewBox="0 0 24 24" aria-hidden="true">
          <path d="M2 5h20v14H2V5zm2 1.8V17h16V6.8l-8 6.1-8-6.1zM5.2 6.5 12 11.7l6.8-5.2H5.2z"/>
        </svg>
        marcus@fernquill.com
      </li>
      <li class="contact-item">
        <svg class="contact-icon" viewBox="0 0 24 24" aria-hidden="true">
          <path d="M12 2a10 10 0 1 0 0 20 10 10 0 0 0 0-20zm-1 17.9A8 8 0 0 1 4.2 10L9 14.8v1c0 1.1.9 2 2 2v2.1zm6.9-2.5c-.3-.8-1-1.4-1.9-1.4h-1v-3c0-.6-.4-1-1-1H8v-2h2c.6 0 1-.4 1-1V7h2c1.1 0 2-.9 2-2v-.4a8 8 0 0 1 2.9 12.8z"/>
        </svg>
        www.fernquill.com
      </li>
    </ul>
  </article>
</main>
</body>
</html>
```